Business Card Design

Supporting people with a spinal cord injury

Industry/Entity Type

Business

Contact Information for Business Card

FRONT
Fiona Lockwood
Service Coordinator
58 Tindal Lane, West Mackay QLD 4740
Tel: (07) 4961 3306
Fax: (07) 4961 3309
after hours: 0498716253
fiona@ktrvb.org.au
www.ktrvb.org.au

BACK - little text to fit
* Personal care and lifestyle assistance
* Supported accommodation - temporary, respite and transition (Cove-lodge)
* Pathway Living Scheme for residents of Cove-lodge with a SCI
* In-home respite support
* Community Access
* In-home support for people in the community
* Wheelchair accessible transport
* Equipment loan
* Use of Keelstep Gym to work on upper body strength
* SCI awareness and prevention
* Information and community linking
* Assist people with obtaining equipment
* 3 accessible, 2bedroom rental units in Andergrove
* After hours emergency support service
BEINF INSPIRED AND INSPIRING OTHERS

```html
<!DOCTYPE html>
<html lang="en">
<head>
<meta charset="utf-8">
<title>KTRVB Business Card</title>
<link href="https://fonts.googleapis.com/css2?family=Exo+2:wght@400;500;600;700&display=swap" rel="stylesheet">
<style>
  :root {
    --backdrop: #a3a3a3;
    --card: #ffffff;
    --orange: #f0a040;
    --orange-deep: #ec9a33;
    --orange-light: #fbe9d4;
    --ink: #2b2b2b;
    --ink-soft: #555555;
    --mark: #8a63b8;
  }
  * { box-sizing: border-box; margin: 0; padding: 0; }
  html, body { width: 1200px; height: 894px; overflow: hidden; }
  body {
    background: radial-gradient(circle at 50% 40%, #b4b4b4, var(--backdrop));
    font-family: "Exo 2", sans-serif;
    color: var(--ink);
    position: relative;
  }
  .card {
    position: absolute;
    top: 287px;
    width: 540px;
    height: 320px;
    background: var(--card);
    overflow: hidden;
    box-shadow: 0 6px 18px rgba(0,0,0,0.18);
  }
  .card--contact { left: 40px; }
  .card--brand { left: 620px; }

  .pill {
    position: absolute;
    right: -40px;
    border-radius: 60px 0 0 60px;
    background: radial-gradient(ellipse at 38% 42%, #fdfaf6 0%, var(--orange-light) 28%, var(--orange) 85%, var(--orange-deep) 100%);
  }
  .card--contact .pill { top: 168px; width: 170px; height: 92px; }
  .card--brand .pill { top: 150px; width: 260px; height: 100px; }

  /* contact side */
  .person { position: absolute; left: 44px; top: 36px; }
  .person__name { font-size: 26px; font-weight: 500; color: var(--orange); letter-spacing: 0.5px; }
  .person__role { font-size: 11px; font-weight: 600; letter-spacing: 1.2px; text-transform: uppercase; color: var(--ink); margin-top: 1px; }
  .rule { position: absolute; height: 2px; background: var(--orange); }
  .rule--name { left: 40px; top: 86px; width: 210px; }
  .rule--details { left: 40px; top: 202px; width: 300px; }
  .rule--address { left: 40px; top: 248px; width: 360px; }
  .rule--foot { left: 40px; top: 290px; width: 410px; }
  .details {
    position: absolute; left: 44px; top: 96px;
    display: grid; grid-template-columns: 88px auto; row-gap: 1px;
    font-size: 14.5px; line-height: 19px;
  }
  .details dt { color: var(--orange); font-weight: 500; }
  .details dd { color: var(--ink); font-weight: 500; letter-spacing: 0.3px; }
  .address {
    position: absolute; left: 40px; top: 214px;
    display: flex; align-items: center; gap: 8px;
    font-size: 14px; font-weight: 500; letter-spacing: 0.3px;
  }

  /* brand side */
  .brand { position: absolute; left: 40px; top: 26px; display: flex; align-items: center; gap: 12px; }
  .brand__dot { width: 48px; height: 48px; border-radius: 50%; background: var(--mark); }
  .brand__name { font-size: 42px; font-weight: 700; color: var(--ink); letter-spacing: 1px; line-height: 1; }
  .brand__tagline { position: absolute; left: 100px; top: 76px; font-size: 8px; color: var(--ink-soft); letter-spacing: 0.3px; }
  .services {
    position: absolute; left: 40px; top: 98px; width: 236px;
    list-style: none;
    font-size: 8px; line-height: 10.6px; font-weight: 500; color: var(--ink);
  }
  .services li { padding-left: 9px; position: relative; }
  .services li::before {
    content: ""; position: absolute; left: 0; top: 3.5px;
    width: 4px; height: 4px; border-radius: 50%; background: var(--orange);
  }
  .motto {
    position: absolute; right: 24px; bottom: 22px;
    font-size: 10px; font-weight: 600; letter-spacing: 1.2px;
    text-transform: uppercase; color: var(--orange);
  }
</style>
</head>
<body>
  <section class="card card--contact" aria-label="Card contact side">
    <div class="person">
      <p class="person__name">Fiona Lockwood</p>
      <p class="person__role">Service Coordinator</p>
    </div>
    <div class="rule rule--name"></div>
    <dl class="details">
      <dt>Phone:</dt><dd>(07) 4961 3306</dd>
      <dt>Fax:</dt><dd>(07) 4961 3309</dd>
      <dt>After hours:</dt><dd>0498716253</dd>
      <dt>Email:</dt><dd>fiona@ktrvb.org.au</dd>
      <dt>website</dt><dd>www.ktrvb.org.au</dd>
    </dl>
    <div class="rule rule--details"></div>
    <p class="address">
      <svg width="14" height="20" viewBox="0 0 14 20" aria-hidden="true">
        <path d="M7 0C3.1 0 0 3.1 0 7c0 5 7 13 7 13s7-8 7-13c0-3.9-3.1-7-7-7z" fill="var(--orange)"/>
        <circle cx="7" cy="7" r="2.6" fill="#fff"/>
      </svg>
      58 Tindal Lane, West Mackay QLD 4740
    </p>
    <div class="rule rule--address"></div>
    <div class="rule rule--foot"></div>
    <div class="pill"></div>
  </section>

  <section class="card card--brand" aria-label="Card brand side">
    <div class="brand">
      <span class="brand__dot"></span>
      <span class="brand__name">KTRVB</span>
    </div>
    <p class="brand__tagline">Kestrel Trail Region Vital Bridges Association</p>
    <ul class="services">
      <li>Personal care and lifestyle assistance</li>
      <li>Supported accommodation – temporary, respite and transition (Cove-lodge)</li>
      <li>Pathway Living Scheme for residents of Cove-lodge with a SCI</li>
      <li>In-home respite support</li>
      <li>Community Access</li>
      <li>In-home support for people in the community</li>
      <li>Wheelchair accessible transport</li>
      <li>Equipment loan</li>
      <li>Use of Keelstep Gym to work on upper body strength</li>
      <li>SCI awareness and prevention</li>
      <li>Information and community linking</li>
      <li>Assist people with obtaining equipment</li>
      <li>3 accessible, 2 bedroom rental units in Andergrove</li>
      <li>After hours emergency support service</li>
    </ul>
    <div class="pill"></div>
    <p class="motto">Being inspired and inspiring others</p>
  </section>
</body>
</html>
```